Outdoor Company Business Card design

We are an outdoor adventure company needing a business card. We sell outdoor adventures and clothing. Please use our logo in the business card. We are looking for something unique but delivers a clear message as to who we are. Please be creative

Target Market(s)

Outdoor adventures

Industry/Entity Type

Business

Contact Information for Business Card

Business name: TrailBirch If using the logo, no need to have a spot for the name
Owner / CEO: Ross Dalby
Website: TrailBirch.example
Facebook: Friendspace.example/TrailBirch
Instagram: @dalby_ross
phone number: 555-304-7192
Email: Dalbycrew@TrailBirch.example

Colors

Designer to choose colors to be used in the design.

Requirements
Must have
• The business card must include the details mentioned above. ie logo, my name, email, facebook, instagram, website, and phone number.
Should not have
• should not be cluttered or look messy

```html
<!DOCTYPE html>
<html lang="en">
<head>
<meta charset="utf-8">
<title>TrailBirch Business Card</title>
<link rel="stylesheet" href="https://fonts.googleapis.com/css2?family=Montserrat:wght@600&family=Open+Sans:wght@400;600&display=swap">
<style>
  :root {
    --brand-blue: #1c74bf;
    --brand-orange: #f15a24;
    --text-grey: #555555;
    --card-white: #ffffff;
    --backdrop: #ebe7e1;
  }
  * { margin: 0; padding: 0; box-sizing: border-box; }
  html, body { width: 1200px; height: 900px; overflow: hidden; }
  body {
    position: relative;
    background: var(--backdrop);
    font-family: "Open Sans", Arial, sans-serif;
    color: var(--text-grey);
  }
  .card {
    position: absolute;
    width: 582px;
    height: 358px;
  }
  .card-front { left: 320px; top: 88px; background: var(--card-white); }
  .card-back { left: 320px; top: 478px; background: var(--brand-blue); }

  .wordmark {
    position: absolute;
    font-family: "Montserrat", Arial, sans-serif;
    font-weight: 600;
    text-transform: uppercase;
    white-space: nowrap;
    line-height: 1;
  }
  .card-front .wordmark {
    right: 32px;
    top: 108px;
    font-size: 44px;
    color: var(--brand-blue);
  }
  .card-back .wordmark {
    left: 0; right: 0;
    top: 206px;
    text-align: center;
    font-size: 62px;
    color: var(--brand-orange);
  }
  .divider {
    position: absolute;
    left: 220px; top: 179px;
    width: 330px; height: 2px;
    background: var(--brand-blue);
  }
  .person { position: absolute; left: 37px; top: 168px; }
  .person-name { font-size: 18px; font-weight: 600; line-height: 24px; }
  .first-name { color: var(--brand-orange); }
  .last-name { color: var(--brand-blue); }
  .person-title { font-size: 14px; line-height: 20px; }

  .contacts {
    position: absolute; left: 37px; top: 235px;
    list-style: none; font-size: 15px; line-height: 21px;
  }
  .contacts li { display: flex; align-items: center; gap: 6px; }
  .contacts svg { width: 13px; height: 13px; fill: var(--brand-orange); }

  .socials {
    position: absolute; right: 32px; top: 254px;
    list-style: none; font-size: 15px; line-height: 22px; text-align: right;
  }
  .socials li { display: flex; align-items: center; justify-content: flex-end; gap: 5px; }
  .social-mark {
    display: inline-block; width: 16px; height: 16px;
    background: var(--brand-orange); border-radius: 3px;
  }
</style>
</head>
<body>
  <section class="card card-front">
    <div class="wordmark">TrailBirch</div>
    <div class="divider"></div>
    <div class="person">
      <p class="person-name"><span class="first-name">Ross</span> <span class="last-name">Dalby</span></p>
      <p class="person-title">Owner / CEO</p>
    </div>
    <ul class="contacts">
      <li>
        <svg viewBox="0 0 16 16" aria-hidden="true"><path d="M2 5c0-2 2-3 6-3s6 1 6 3v1h-3V5H5v1H2zM3 8l2-2h6l2 2v6H3z"/></svg>
        555-304-7192
      </li>
      <li>
        <svg viewBox="0 0 16 16" aria-hidden="true"><path d="M1 3h14v10H1z M1 3l7 6 7-6" stroke="#fff" stroke-width="1"/></svg>
        Dalbycrew@TrailBirch.example
      </li>
      <li>
        <svg viewBox="0 0 16 16" aria-hidden="true"><circle cx="8" cy="8" r="7"/><path d="M1 8h14M8 1c3 3 3 11 0 14M8 1c-3 3-3 11 0 14" stroke="#fff" stroke-width="1" fill="none"/></svg>
        www.TrailBirch.example
      </li>
    </ul>
    <ul class="socials">
      <li>Friendspace.example/TrailBirch <span class="social-mark"></span></li>
      <li>@dalby_ross <span class="social-mark"></span></li>
    </ul>
  </section>

  <section class="card card-back">
    <div class="wordmark">TrailBirch</div>
  </section>
</body>
</html>
```